indépendant en tant que Massothérapeute et Préparateur Mental, j'ai besoin de ...

Massothérapeute et préparateur mental indépendant, je recherche une carte de visite sobre et dynamique, sans images liées au massage ou à la préparation mentale mais intégrant mon logo. Les couleurs que j'aime bien sont : Blanc, gris, anthracite, noir et jaune

Contact Information for Business Card

carte de préférence Horizontale
neutre qui puisse toucher le deux domaines Massothérapie et préparation mentale

Requirements
Must have
• mon projet doit intégrer au recto:
LOGO
Loïc Vermande
078 315 26 49
info@loicvermande-exemple.ch
et éventuellement www.loicvermande-exemple.ch

et au verso les deux adresses:

Chemin des Ormelets 27B
1400 Yverdon-les-Bains

Rue des Tanneries 9
1700 Fribourg

Should not have
• mon projet ne doit pas contenir d'image en liens avec le massage ni la préparation mentale.

```html
<!DOCTYPE html>
<html lang="fr">
<head>
<meta charset="utf-8">
<title>Carte de visite – Loïc Vermande</title>
<link href="https://fonts.googleapis.com/css2?family=Work+Sans:wght@400;500;600&display=swap" rel="stylesheet">
<style>
  :root {
    --page: #3a3a3a;
    --card-dark: #1f1f1f;
    --card-dark-2: #2b2b2b;
    --light-1: #ecebea;
    --light-2: #cfc7c2;
    --ink: #1e1e1e;
    --white: #ffffff;
    --yellow: #f2b705;
    --muted: #d9d9d9;
  }
  * { margin: 0; padding: 0; box-sizing: border-box; }
  html, body { width: 1200px; height: 930px; overflow: hidden; }
  body {
    background: var(--page);
    font-family: "Work Sans", sans-serif;
    position: relative;
  }
  .card {
    position: absolute;
    left: 250px;
    width: 700px;
    height: 400px;
    border-radius: 18px;
    overflow: hidden;
  }
  .card--front { top: 40px; background: var(--light-1); }
  .card--back {
    top: 490px;
    background: linear-gradient(135deg, var(--card-dark) 0%, var(--card-dark-2) 55%, var(--card-dark) 100%);
    color: var(--white);
  }
  .front-photo {
    position: absolute; inset: 0;
    background: radial-gradient(ellipse at 55% 60%, #e6dcd6 0%, var(--light-2) 45%, #b9b0ab 75%, var(--light-1) 100%);
    opacity: .75;
  }
  .brand {
    position: absolute;
    display: flex;
    align-items: center;
    gap: 12px;
  }
  .brand__dot { width: 16px; height: 16px; border-radius: 50%; flex: none; }
  .brand__text { display: flex; flex-direction: column; }
  .brand__name { font-weight: 600; letter-spacing: .5px; line-height: 1; }
  .brand__tagline { font-size: 9px; letter-spacing: 1px; text-transform: uppercase; margin-top: 5px; }
  .card--front .brand { left: 190px; top: 176px; color: var(--ink); }
  .card--front .brand__dot { background: var(--ink); width: 22px; height: 22px; }
  .card--front .brand__name { font-size: 34px; }
  .card--front .brand__tagline { font-size: 11px; }
  .card--back .brand { left: 360px; top: 36px; color: var(--white); }
  .card--back .brand__dot { background: var(--white); }
  .card--back .brand__name { font-size: 22px; }
  .holder { position: absolute; left: 60px; top: 190px; }
  .holder__bar { position: absolute; left: -60px; top: 8px; width: 12px; height: 44px; background: var(--yellow); }
  .holder__name { font-size: 27px; font-weight: 500; color: var(--yellow); letter-spacing: 1px; text-transform: uppercase; }
  .holder__role { font-size: 18px; color: var(--white); margin-top: 2px; }
  .rule { position: absolute; height: 1.5px; background: var(--yellow); }
  .rule--main { left: 60px; right: 60px; top: 262px; }
  .rule--short { right: 60px; width: 30px; top: 326px; }
  .addresses {
    position: absolute; right: 60px; top: 276px;
    text-align: right; font-size: 15px; line-height: 1.35; color: var(--muted);
  }
  .addresses p + p { margin-top: 16px; }
  .contacts { position: absolute; left: 60px; top: 290px; list-style: none; font-size: 17px; line-height: 1.5; }
  .contacts li { display: flex; align-items: center; gap: 10px; }
  .contacts svg { width: 13px; height: 13px; flex: none; }
</style>
</head>
<body>
  <section class="card card--front" aria-label="Recto">
    <div class="front-photo" role="img" aria-label="Photographie d'ambiance adoucie, tons gris et beige"></div>
    <div class="brand">
      <span class="brand__dot"></span>
      <div class="brand__text">
        <span class="brand__name">Loïc Vermande</span>
        <span class="brand__tagline">Massothérapeute / Préparateur Mental</span>
      </div>
    </div>
  </section>

  <section class="card card--back" aria-label="Verso">
    <div class="brand">
      <span class="brand__dot"></span>
      <div class="brand__text">
        <span class="brand__name">Loïc Vermande</span>
        <span class="brand__tagline">Massothérapeute / Préparateur Mental</span>
      </div>
    </div>

    <div class="holder">
      <span class="holder__bar"></span>
      <h1 class="holder__name">Loïc Vermande</h1>
      <p class="holder__role">Director</p>
    </div>

    <div class="rule rule--main"></div>

    <div class="addresses">
      <p>Chemin des Ormelets 27B<br>1400 Yverdon-les-Bains</p>
      <p>Rue des Tanneries 9<br>1700 Fribourg</p>
    </div>
    <div class="rule rule--short"></div>

    <ul class="contacts">
      <li>
        <svg viewBox="0 0 24 24" fill="#f2b705"><path d="M6.6 10.8a15.1 15.1 0 0 0 6.6 6.6l2.2-2.2a1 1 0 0 1 1-.25 11.4 11.4 0 0 0 3.6.57 1 1 0 0 1 1 1V20a1 1 0 0 1-1 1A17 17 0 0 1 3 4a1 1 0 0 1 1-1h3.5a1 1 0 0 1 1 1c0 1.25.2 2.45.57 3.57a1 1 0 0 1-.25 1z"/></svg>
        078 315 26 49
      </li>
      <li>
        <svg viewBox="0 0 24 24" fill="none" stroke="#f2b705" stroke-width="2.4"><rect x="3" y="5" width="18" height="14" rx="1"/><path d="M3 6l9 7 9-7"/></svg>
        info@loicvermande-exemple.ch
      </li>
      <li>
        <svg viewBox="0 0 24 24" fill="none" stroke="#f2b705" stroke-width="2.2"><circle cx="12" cy="12" r="9"/><path d="M3 12h18M12 3c3 3 3 15 0 18M12 3c-3 3-3 15 0 18"/></svg>
        www.loicvermande-exemple.ch
      </li>
    </ul>
  </section>
</body>
</html>
```